Organizational health infographic

I work as an independent contractor with a larger consulting firm named "the Lantern Works" https://www.lanternworks-example.com/ I need a simple infographic that visually explains the 3 stages of our client engagement, and their respective steps and objectives. Im inclined to use a "subway" map system design (Ive included a a draft overview of the content (in PPT and a PDF) and b) a few sample subway style infographics. I

Target Market(s)

CEOs and Human Resources Officers

Font styles to use
Sans Serif

Colors

Designer to choose colors to be used in the design.

Requirements
Must have
• my contact info
• martin kell 555-304-8821
• martin.kell@lanternworksadvisory-example.com
• lantern works logo (I put it near the top center part of the page). Logo and book pictures can be found on the website https://www.lanternworks-example.com
Nice to have
• 1) the more consistent the font and colors are with the Lantern Works website, the better https://www.lanternworks-example.com
• 2) if its possible to have all 3 "subway lines" collapse into a single timeline, that would be cool.
• 3) If its possible to add a visual timeline that shows each stage taking approx 3 to 6 months, also cool.
• 4) in stage 3, Im not sure about whether to use the actual book pictures or simply the titles of each book at a "subway stop" circle.

```html
<!DOCTYPE html>
<html lang="en">
<head>
<meta charset="utf-8">
<title>Lantern Works – Client Engagement Map</title>
<link rel="stylesheet" href="https://fonts.googleapis.com/css2?family=Montserrat:wght@400;600;700;800&family=Open+Sans:wght@400;600;700&display=swap">
<style>
  :root{
    --ink:#2b3040;
    --footer:#262b3a;
    --red:#c8373d;
    --green:#8dc63f;
    --blue:#29a8e0;
    --paper:#ffffff;
  }
  *{margin:0;padding:0;box-sizing:border-box}
  html,body{width:776px;height:1200px;overflow:hidden;background:var(--paper)}
  body{position:relative;font-family:"Open Sans",Arial,sans-serif;color:var(--ink)}
  .brand-band{position:absolute;left:0;top:50px;width:266px;height:33px;background:var(--ink);display:flex;align-items:center;padding-left:38px;gap:8px}
  .brand-dot{width:20px;height:20px;border-radius:50%;background:var(--red)}
  .brand-name{font-family:"Montserrat",sans-serif;font-weight:600;font-size:23px;color:#fff;letter-spacing:-.3px}
  .contact{position:absolute;right:43px;top:30px;text-align:right}
  .contact-name{font-family:"Montserrat",sans-serif;font-size:52px;line-height:1;letter-spacing:-1px}
  .contact-name .first{color:var(--red);font-weight:800}
  .contact-name .last{color:var(--ink);font-weight:400}
  .contact-line{font-family:"Montserrat",sans-serif;font-weight:700;font-size:15px;line-height:18px;color:var(--ink)}
  .contact-line:first-of-type{margin-top:8px}
  .rule{position:absolute;left:43px;top:164px;width:690px;height:3px;background:var(--ink)}
  .map{position:absolute;left:0;top:0}
  .map text{font-family:"Open Sans",Arial,sans-serif;fill:var(--ink)}
  .stage-title{font-family:"Montserrat",sans-serif !important;font-weight:800;font-size:24px;letter-spacing:3px}
  .stage-tag{font-family:"Montserrat",sans-serif !important;font-weight:600;font-size:15px;fill:#fff !important}
  .stop-label{font-size:10px}
  .hub-label{font-weight:700;font-size:13px}
  .objectives{position:absolute;left:488px;width:270px}
  .obj-heading{font-family:"Montserrat",sans-serif;font-weight:700;font-size:17px;letter-spacing:4px;margin-bottom:6px}
  .obj-group{margin-bottom:6px}
  .obj-group h3{font-family:"Montserrat",sans-serif;font-weight:700;font-size:13px;line-height:17px}
  .obj-group ul{list-style:none;margin-left:6px}
  .obj-group li{font-size:11px;line-height:14.5px;padding-left:10px;position:relative}
  .obj-group li::before{content:"";position:absolute;left:0;top:5px;width:4px;height:4px;border-radius:50%;background:var(--accent)}
  .obj-red{top:232px;--accent:var(--red)} .obj-red .obj-heading{color:var(--red)}
  .obj-green{top:493px;--accent:var(--green)} .obj-green .obj-heading{color:var(--green)}
  .obj-blue{top:787px;--accent:var(--blue)} .obj-blue .obj-heading{color:var(--blue)}
  .obj-blue .obj-group{margin-bottom:10px}
  .footer{position:absolute;left:0;top:1080px;width:776px;height:120px;background:var(--footer)}
  .legend{position:absolute;left:52px;top:34px;display:flex;gap:10px}
  .legend-item{width:56px;display:flex;flex-direction:column;align-items:center;gap:6px}
  .legend-item span{font-family:"Montserrat",sans-serif;font-weight:600;font-size:7.5px;line-height:9px;color:#fff;text-align:center;letter-spacing:.5px}
  .footer-divider{position:absolute;left:323px;top:28px;width:3px;height:66px;background:#fff}
  .footer-url{position:absolute;left:355px;top:46px;font-family:"Montserrat",sans-serif;font-weight:700;font-size:21px;color:#fff}
</style>
</head>
<body>
  <header>
    <div class="brand-band"><span class="brand-dot"></span><span class="brand-name">lantern works</span></div>
    <div class="contact">
      <div class="contact-name"><span class="first">martin</span> <span class="last">kell</span></div>
      <div class="contact-line">555-304-8821</div>
      <div class="contact-line">martin.kell@lanternworksadvisory-example.com</div>
    </div>
    <div class="rule"></div>
  </header>

  <svg class="map" width="776" height="1080" viewBox="0 0 776 1080" aria-label="Three-stage engagement route map">
    <g fill="none" stroke="var(--ink)" stroke-width="3" stroke-dasharray="7 6">
      <path d="M412 242 H352 M148 242 H90 Q78 242 78 254 V340"/>
      <path d="M424 386 V470 Q424 482 412 482 H352 M148 482 H90 Q78 482 78 494 V594"/>
      <path d="M424 637 V760 Q424 772 412 772 H352 M148 772 H90 Q78 772 78 784 V897"/>
    </g>
    <g fill="none" stroke="var(--ink)" stroke-width="3">
      <path d="M101 363 H405"/>
      <path d="M95 601 L163 567 H410 Q424 567 424 581 V597"/>
      <path d="M95 633 L163 674 H335"/>
      <path d="M95 905 L150 868 H410 Q424 868 424 882 V905"/>
      <path d="M95 936 L150 982 H410 Q424 982 424 968 V948"/>
    </g>

    <!-- Stage 1 -->
    <text class="stage-title" x="252" y="236" text-anchor="middle">STAGE 1</text>
    <rect x="148" y="239" width="204" height="22" fill="var(--red)"/>
    <text class="stage-tag" x="250" y="255" text-anchor="middle">Excutive Launch</text>
    <circle cx="424" cy="242" r="12" fill="var(--red)"/>
    <g stroke="var(--red)" stroke-width="3" fill="#fff">
      <circle cx="78" cy="363" r="23"/>
      <circle cx="327" cy="363" r="20"/>
      <path d="M400 343 H448 L424 384 Z"/>
    </g>
    <circle cx="183" cy="363" r="12" fill="var(--red)"/>
    <circle cx="246" cy="363" r="12" fill="var(--red)"/>
    <text class="hub-label" x="78" y="405" text-anchor="middle">2 Day</text>
    <text class="stop-label" x="183" y="397" text-anchor="middle">Meeting</text>
    <text class="stop-label" x="183" y="409" text-anchor="middle">Audits</text>
    <text class="stop-label" x="246" y="397" text-anchor="middle">Leader</text>
    <text class="stop-label" x="246" y="409" text-anchor="middle">Coaching</text>
    <text class="stop-label" x="327" y="397" text-anchor="middle">Quarterly</text>
    <text class="stop-label" x="327" y="409" text-anchor="middle">Off Sites</text>

    <!-- Stage 2 -->
    <text class="stage-title" x="252" y="477" text-anchor="middle">STAGE 2</text>
    <rect x="148" y="478" width="204" height="22" fill="var(--green)"/>
    <text class="stage-tag" x="250" y="494" text-anchor="middle">Next Level Rollout</text>
    <rect x="163" y="527" width="172" height="17" rx="8.5" fill="var(--ink)"/>
    <text x="249" y="540" text-anchor="middle" style="fill:#fff;font-size:11px">Key leader conferences</text>
    <g stroke="var(--green)" stroke-width="3" fill="#fff">
      <circle cx="78" cy="617" r="23"/>
      <circle cx="163" cy="567" r="14"/>
      <circle cx="249" cy="567" r="14"/>
      <circle cx="335" cy="567" r="14"/>
      <circle cx="163" cy="674" r="19"/>
      <circle cx="335" cy="674" r="19"/>
      <path d="M400 595 H448 L424 637 Z"/>
    </g>
    <circle cx="220" cy="674" r="10" fill="var(--green)"/>
    <circle cx="278" cy="674" r="10" fill="var(--green)"/>
    <text class="hub-label" x="78" y="661" text-anchor="middle">Key Leader</text>
    <text class="hub-label" x="78" y="677" text-anchor="middle">Kickoff</text>
    <text class="stop-label" x="220" y="644" text-anchor="middle">Meeting</text>
    <text class="stop-label" x="220" y="656" text-anchor="middle">Audits</text>
    <text class="stop-label" x="278" y="644" text-anchor="middle">Leader</text>
    <text class="stop-label" x="278" y="656" text-anchor="middle">Coaching</text>
    <text class="stop-label" x="163" y="710" text-anchor="middle">Department</text>
    <text class="stop-label" x="163" y="722" text-anchor="middle">Team Offsites</text>
    <text class="stop-label" x="335" y="710" text-anchor="middle">Department</text>
    <text class="stop-label" x="335" y="722" text-anchor="middle">Rollouts</text>

    <!-- Stage 3 -->
    <text class="stage-title" x="252" y="767" text-anchor="middle">STAGE 3</text>
    <rect x="148" y="768" width="204" height="22" fill="var(--blue)"/>
    <text class="stage-tag" x="250" y="784" text-anchor="middle">Organizational Rollout</text>
    <g stroke="var(--blue)" stroke-width="3" fill="#fff">
      <circle cx="78" cy="920" r="23"/>
      <rect x="150" y="855" width="26" height="26"/>
      <rect x="150" y="969" width="26" height="26"/>
      <circle cx="223" cy="868" r="11"/>
      <circle cx="269" cy="868" r="11"/>
      <circle cx="314" cy="868" r="11"/>
      <circle cx="362" cy="868" r="11"/>
      <circle cx="353" cy="982" r="11"/>
      <path d="M400 905 H448 L424 946 Z"/>
    </g>
    <text class="hub-label" x="78" y="964" text-anchor="middle">Playbook</text>
    <text class="hub-label" x="78" y="980" text-anchor="middle">Rollout</text>
    <text class="stop-label" x="163" y="897" text-anchor="middle">Workshops</text>
    <text class="stop-label" x="223" y="820" text-anchor="middle">The Quiet</text>
    <text class="stop-label" x="223" y="832" text-anchor="middle">Gaps In</text>
    <text class="stop-label" x="223" y="844" text-anchor="middle">A Team</text>
    <text class="stop-label" x="314" y="820" text-anchor="middle">The Honest</text>
    <text class="stop-label" x="314" y="832" text-anchor="middle">Side Of Staff</text>
    <text class="stop-label" x="314" y="844" text-anchor="middle">Morale</text>
    <text class="stop-label" x="269" y="897" text-anchor="middle">The Steady</text>
    <text class="stop-label" x="269" y="909" text-anchor="middle">Teammate</text>
    <text class="stop-label" x="362" y="897" text-anchor="middle">Lost In</text>
    <text class="stop-label" x="362" y="909" text-anchor="middle">Meetings</text>
    <text class="stop-label" x="210" y="976">Train the trainers</text>
    <text class="stop-label" x="210" y="995">Train the leaders</text>
    <text class="stop-label" x="163" y="1009" text-anchor="middle">Internal</text>
    <text class="stop-label" x="163" y="1021" text-anchor="middle">Training</text>
    <text class="stop-label" x="353" y="1011" text-anchor="middle">Closing The</text>
    <text class="stop-label" x="353" y="1023" text-anchor="middle">Quiet Gaps</text>
    <text class="stop-label" x="353" y="1035" text-anchor="middle">In A Team</text>
  </svg>

  <section class="objectives obj-red">
    <h2 class="obj-heading">OBJECTIVES</h2>
    <div class="obj-group"><h3>Team cohesion</h3><ul><li>Solid trust</li><li>Aligned expectations</li></ul></div>
    <div class="obj-group"><h3>Playbook 1.0</h3><ul><li>Aligned vision, values, strategy,<br>priorities &amp; roles</li></ul></div>
    <div class="obj-group"><h3>Productive meetings</h3><ul><li>Consistent communication with greater org</li></ul></div>
    <div class="obj-group"><h3>Transition readiness</h3><ul><li>Cohesion validation (CTAR)</li><li>Playbook Complete</li><li>Meeting Momentum</li></ul></div>
  </section>

  <section class="objectives obj-green">
    <h2 class="obj-heading">OBJECTIVES</h2>
    <div class="obj-group"><h3>Key leaders</h3><ul><li>Finish Playbook 2.0</li><li>Become Ambassadors Of Org Health</li><li>Cross Functional Cooperation Playbook 2.0</li></ul></div>
    <div class="obj-group"><h3>Department teams</h3><ul><li>Cohesion, Clarity, Productive Meetings</li></ul></div>
    <div class="obj-group"><h3>Department rollouts</h3><ul><li>Break Down Silos</li><li>Dept Priorities Align To Org Priorities</li></ul></div>
    <div class="obj-group"><h3>Transition readiness</h3><ul><li>Ctars Department</li><li>Core Values Detailed And Implemented</li><li>Meeting Mastery</li></ul></div>
  </section>

  <section class="objectives obj-blue">
    <h2 class="obj-heading">OBJECTIVES</h2>
    <div class="obj-group"><h3>All employees</h3><ul><li>Understand and utilize the playbook<br>Are equipped &amp; motivated to create a<br>healthy culture</li></ul></div>
    <div class="obj-group"><h3>Transition readiness</h3><ul><li>The consultation is completed when the<br>leaders are ready to assume responsibility<br>for maintaining a healthy culture.</li></ul></div>
  </section>

  <footer class="footer">
    <div class="legend">
      <div class="legend-item"><svg width="28" height="28"><circle cx="14" cy="14" r="12" fill="none" stroke="#fff" stroke-width="3"/></svg><span>Live Off Site</span></div>
      <div class="legend-item"><svg width="28" height="28"><circle cx="14" cy="14" r="13" fill="#fff"/></svg><span>Video<br>Conference</span></div>
      <div class="legend-item"><svg width="28" height="28"><path d="M2 3 H26 L14 25 Z" fill="none" stroke="#fff" stroke-width="3"/></svg><span>Transition<br>Evaluation</span></div>
      <div class="legend-item"><svg width="28" height="28"><rect x="3" y="3" width="22" height="22" fill="none" stroke="#fff" stroke-width="3"/></svg><span>Training</span></div>
    </div>
    <div class="footer-divider"></div>
    <div class="footer-url">www.lanternworks-example.com</div>
  </footer>
</body>
</html>
```